CLICK HERE TO MEET ADVISOR ON VIDEO CALL

1. Our company (Talknest) is like PLINK but for online shoppers to Click the Graphic Link You Will Be Designing.
2. Copy for the link would invite online shopper to CLICK TO MEET OUR ADVISOR
3. If shopper clicks on the link, instantly they would meet our clients sales advisor on a 2-way video call. OUR BUSINESS IS IN ROUTING SHOPPERS TO ADVISORS ON VIDEO-SALES-CALLS
3. The Graphic you design would be placed on websites, emails, digital ads, etc.
4. In your graphic we want to INVITE THE SHOPPER TO CLICK, and SHOW WHAT A 2-WAY VIDEO CALL WOULD LOOK LIKE.
5. THERE IS 1 GRAPHIC ALREADY BEING USED IN CAR DEALERSHIPS. See: WWW.MARLOWAUTOS.NET and the current graphic will appear in lower left corner of their website home page.
6. We need a graphic for a white casually dressed male Real Estate Agent on a cell phone meeting with an African American mid 30s couple who are seeing the agent on their laptop

CLICK HERE TO MEET OUR ADVISOR

```html
<!DOCTYPE html>
<html lang="en">
<head>
<meta charset="utf-8">
<title>Click Here to Meet Our Advisor</title>
<link href="https://fonts.googleapis.com/css2?family=Montserrat:wght@800;900&display=swap" rel="stylesheet">
<style>
  :root {
    --page: #ffffff;
    --card: #f8f8f8;
    --brand-blue: #2e3192;
    --ink: #0a0a0a;
    --bezel: #0d0d0d;
    --aluminium: #c9cacc;
    --phone-frame: #3a2a35;
    --control-bg: #f4f4f4;
    --control-icon: #555555;
    --hangup: #e8232f;
    --glove: #ffffff;
  }
  html, body {
    margin: 0;
    padding: 0;
    width: 1200px;
    height: 1200px;
    overflow: hidden;
    background: var(--page);
  }
  .banner {
    display: block;
    width: 1200px;
    height: 1200px;
    font-family: "Montserrat", Arial, sans-serif;
  }
  .headline { fill: var(--brand-blue); font-weight: 900; }
  .subline { fill: var(--ink); font-weight: 800; }
</style>
</head>
<body>
<svg class="banner" viewBox="0 0 1200 1200" xmlns="http://www.w3.org/2000/svg">
  <defs>
    <linearGradient id="couple-scene" x1="0" y1="0" x2="1" y2="1">
      <stop offset="0" stop-color="#ece6df"/>
      <stop offset="0.5" stop-color="#b07a64"/>
      <stop offset="1" stop-color="#8d3b4a"/>
    </linearGradient>
    <linearGradient id="agent-scene" x1="0" y1="0" x2="0" y2="1">
      <stop offset="0" stop-color="#e4ebef"/>
      <stop offset="0.45" stop-color="#c9b3a5"/>
      <stop offset="1" stop-color="#1c1f2a"/>
    </linearGradient>
    <linearGradient id="laptop-base" x1="0" y1="0" x2="0" y2="1">
      <stop offset="0" stop-color="#e6e7e9"/>
      <stop offset="1" stop-color="#8d8e91"/>
    </linearGradient>
    <filter id="soft-shadow" x="-50%" y="-50%" width="200%" height="200%">
      <feDropShadow dx="14" dy="22" stdDeviation="16" flood-color="#000" flood-opacity="0.28"/>
    </filter>
  </defs>

  <!-- card -->
  <rect class="card" x="78" y="351" width="1045" height="478" rx="68" fill="var(--card)"/>

  <!-- laptop -->
  <g class="laptop">
    <rect x="130" y="447" width="300" height="268" rx="8" fill="var(--bezel)"/>
    <circle cx="333" cy="455" r="1.8" fill="#333"/>
    <rect x="146" y="465" width="280" height="236" fill="url(#couple-scene)" role="img" aria-label="Photo of a smiling couple on a sofa watching a video call on their laptop"/>
    <path d="M85 716 H430 V733 H112 Q88 733 85 725 Z" fill="url(#laptop-base)"/>
    <rect x="294" y="716" width="78" height="6" rx="3" fill="#a9aaad"/>
    <g class="call-controls">
      <rect x="281" y="669" width="113" height="22" rx="11" fill="var(--control-bg)"/>
      <rect x="293" y="677" width="6" height="5" fill="var(--control-icon)"/>
      <rect x="314" y="675" width="3" height="7" rx="1.5" fill="var(--control-icon)"/>
      <circle cx="337" cy="680" r="8.5" fill="var(--hangup)"/>
      <path d="M333 681 Q337 676 341 681" stroke="#fff" stroke-width="1.6" fill="none"/>
      <circle cx="358" cy="678" r="2" fill="var(--control-icon)"/>
      <path d="M355 684 Q358 680 361 684 Z" fill="var(--control-icon)"/>
      <circle cx="375" cy="680" r="1" fill="var(--control-icon)"/>
      <circle cx="378" cy="680" r="1" fill="var(--control-icon)"/>
      <circle cx="381" cy="680" r="1" fill="var(--control-icon)"/>
    </g>
  </g>

  <!-- phone -->
  <g class="phone">
    <rect x="420" y="430" width="154" height="318" rx="24" fill="var(--phone-frame)"/>
    <rect x="424" y="434" width="146" height="310" rx="21" fill="var(--bezel)"/>
    <rect x="428" y="440" width="138" height="300" rx="17" fill="url(#agent-scene)" role="img" aria-label="Photo of a smiling advisor in a suit talking on his phone"/>
    <g class="call-controls">
      <rect x="440" y="708" width="64" height="22" rx="11" fill="var(--control-bg)"/>
      <rect x="453" y="716" width="6" height="5" fill="var(--control-icon)"/>
      <rect x="474" y="714" width="3" height="7" rx="1.5" fill="var(--control-icon)"/>
    </g>
  </g>

  <!-- click pointer -->
  <g class="click-pointer">
    <g class="click-rays" stroke="var(--brand-blue)" stroke-width="8" stroke-linecap="round">
      <line x1="480" y1="621" x2="485" y2="634"/>
      <line x1="504" y1="614" x2="501" y2="628"/>
      <line x1="526" y1="631" x2="517" y2="638"/>
      <line x1="458" y1="639" x2="470" y2="643"/>
      <line x1="459" y1="668" x2="470" y2="662"/>
    </g>
    <g transform="translate(493 652) rotate(-28)" filter="url(#soft-shadow)">
      <path d="M0,100 L0,13 A13,13 0 0 1 26,13 L26,60 A12,12 0 0 1 50,60 L50,66 A12,12 0 0 1 74,66 L74,72 A12,12 0 0 1 98,72 L98,120 Q98,150 80,165 L80,178 L20,178 L20,165 L-20,120 A14,14 0 0 1 0,100 Z"
            transform="translate(-13 0)" fill="var(--glove)" stroke="var(--brand-blue)" stroke-width="9" stroke-linejoin="round"/>
      <g transform="translate(-13 0)" stroke="var(--brand-blue)" stroke-width="7" stroke-linecap="round">
        <line x1="26" y1="60" x2="26" y2="90"/>
        <line x1="50" y1="66" x2="50" y2="92"/>
        <line x1="74" y1="72" x2="74" y2="96"/>
      </g>
    </g>
  </g>

  <!-- copy -->
  <g class="cta-copy">
    <text class="headline" x="640" y="554" font-size="152" textLength="427" lengthAdjust="spacingAndGlyphs">CLICK</text>
    <text class="headline" x="660" y="671" font-size="152" textLength="380" lengthAdjust="spacingAndGlyphs">HERE</text>
    <text class="subline" x="637" y="722" font-size="38" textLength="436" lengthAdjust="spacingAndGlyphs">TO MEET OUR ADVISOR</text>
  </g>
</svg>
</body>
</html>
```